Business Card Design

We need a design for business cards for our company. We have a logo. We teach EMT's and we are based out of Virginia. The information that will need to add would be, name, title, phone number, email, address. On the back of the business card would be "We help you, help others"

Target Market(s)

People that want to become EMT's

Colors

Designer to choose colors to be used in the design.

Requirements
Must have
• company logo

```html
<!DOCTYPE html>
<html lang="en">
<head>
<meta charset="utf-8">
<title>Rescue Ready Academy – Business Card</title>
<link href="https://fonts.googleapis.com/css2?family=Montserrat:wght@400;600;700&display=swap" rel="stylesheet">
<style>
  :root {
    --page-bg: #2b2d30;
    --card-white: #ffffff;
    --card-navy: #1f2a33;
    --brand-red: #c8202f;
    --text-grey: #4a4d52;
    --text-light: #ffffff;
  }
  * { margin: 0; padding: 0; box-sizing: border-box; }
  html, body {
    width: 1200px; height: 900px; overflow: hidden;
    background: var(--page-bg);
    font-family: "Montserrat", Arial, sans-serif;
  }
  .canvas { position: relative; width: 1200px; height: 900px; }
  .card {
    position: absolute; left: 280px; width: 640px; height: 366px;
    border-radius: 4px; overflow: hidden;
  }
  .card--back { top: 60px; background: var(--card-navy); }
  .card--front { top: 474px; background: var(--card-white); }

  .brand {
    display: flex; align-items: center; gap: 12px;
    color: var(--brand-red); font-weight: 700; font-size: 30px;
    letter-spacing: 0.5px; text-transform: uppercase;
  }
  .brand__mark { width: 22px; height: 22px; background: var(--brand-red); flex: none; }

  .card--back .brand {
    position: absolute; top: 130px; left: 0; right: 0; justify-content: center;
  }
  .tagline {
    position: absolute; top: 230px; left: 0; right: 0; text-align: center;
    color: var(--text-light); font-weight: 600; font-size: 15px;
    letter-spacing: 4px; text-transform: uppercase;
  }

  .card--front .brand { position: absolute; top: 60px; left: 48px; font-size: 26px; }
  .name-band {
    position: absolute; top: 168px; left: 330px; right: 0; height: 74px;
    background: var(--brand-red); color: var(--text-light);
    padding: 12px 0 0 28px;
  }
  .name-band__name { font-weight: 700; font-size: 24px; letter-spacing: 1px; text-transform: uppercase; }
  .name-band__title { font-weight: 400; font-size: 17px; margin-top: 2px; }
  .contact { position: absolute; top: 262px; left: 312px; list-style: none; }
  .contact__item {
    display: flex; align-items: center; gap: 12px;
    color: var(--text-grey); font-size: 19px; margin-bottom: 10px;
  }
  .contact__icon { width: 18px; height: 18px; flex: none; }
</style>
</head>
<body>
<main class="canvas">
  <section class="card card--back" aria-label="Card back">
    <div class="brand"><span class="brand__mark"></span>Rescue Ready Academy</div>
    <p class="tagline">We help you, help others</p>
  </section>

  <section class="card card--front" aria-label="Card front">
    <div class="brand"><span class="brand__mark"></span>Rescue Ready Academy</div>
    <div class="name-band">
      <div class="name-band__name">Daniel Reyes</div>
      <div class="name-band__title">Sales Manager</div>
    </div>
    <ul class="contact">
      <li class="contact__item">
        <svg class="contact__icon" viewBox="0 0 24 24" fill="none" stroke="#c8202f" stroke-width="2">
          <circle cx="12" cy="12" r="10"/>
          <path d="M8.5 7.5l2 2-1.2 1.5c.8 1.6 2 2.8 3.6 3.6l1.5-1.2 2 2-1.3 1.6c-3.8-.6-7-3.8-7.6-7.6z"/>
        </svg>
        555-210-4830
      </li>
      <li class="contact__item">
        <svg class="contact__icon" viewBox="0 0 24 24" fill="none" stroke="#c8202f" stroke-width="2">
          <rect x="3" y="5" width="18" height="14"/>
          <path d="M3 5l9 8 9-8"/>
        </svg>
        hello@rescueready.com
      </li>
    </ul>
  </section>
</main>
</body>
</html>
```